Wedding invitation

We need a wedding invitation designed with a logo using our initials and name underneath.
We are getting married at THE VERDELLE hotel in Gstaad and we would like have our logo similar to theirs but incorporating our initials n&l (any font/case) and our names below nuriya and Laurent. The Verdelle logo can be seen on their website.
The invitation would be square with the logo on the front in stamped foil and the colour would be THE VERDELLE brown (I have the exact colour)
THE VERDELLE Brown: C45 M70 Y68 K77
THE VERDELLE Rose Gold: BRENVIK 812
Inside we would have the invitation wording and on the opposite side some contact info. There would be four inserts - accom, directions, brunch and RSVP. We will provide the wording.

```html
<!DOCTYPE html>
<html lang="en">
<head>
<meta charset="utf-8">
<title>Invitation – Nuriya and Laurent</title>
<link rel="stylesheet" href="https://fonts.googleapis.com/css2?family=Cormorant+Garamond:wght@400&family=Josefin+Sans:wght@300&family=La+Belle+Aurore&display=swap">
<style>
  :root {
    --paper: #ffffff;
    --verdelle-brown: #3e1f1a;
    --ink-script: #4a2f2a;
    --on-brown: #fbf6f2;
  }
  html, body {
    margin: 0;
    padding: 0;
    overflow: hidden;
    background: var(--paper);
  }
  .invitation-front {
    position: relative;
    width: 1200px;
    height: 1200px;
    background: var(--paper);
    overflow: hidden;
  }
  .invitation-title {
    position: absolute;
    top: 92px;
    left: 0;
    width: 1200px;
    margin: 0;
    text-align: center;
    font-family: "Cormorant Garamond", Georgia, serif;
    font-weight: 400;
    font-size: 58px;
    letter-spacing: 0.62em;
    padding-left: 0.62em;
    box-sizing: border-box;
    color: var(--verdelle-brown);
    line-height: 1;
  }
  .monogram-seal {
    position: absolute;
    left: 360px;
    top: 363px;
    width: 480px;
    height: 480px;
    border-radius: 50%;
    background: var(--verdelle-brown);
    display: flex;
    align-items: center;
    justify-content: center;
  }
  .monogram-initials {
    font-family: "Josefin Sans", "Helvetica Neue", sans-serif;
    font-weight: 300;
    font-size: 104px;
    letter-spacing: 0.06em;
    color: var(--on-brown);
    line-height: 1;
    margin: 0;
    padding-top: 12px;
  }
  .couple-names {
    position: absolute;
    top: 1020px;
    left: 0;
    width: 1200px;
    margin: 0;
    text-align: center;
    font-family: "La Belle Aurore", cursive;
    font-weight: 400;
    font-size: 62px;
    color: var(--ink-script);
    line-height: 1.2;
  }
</style>
</head>
<body>
  <main class="invitation-front">
    <h1 class="invitation-title">INVITATION</h1>
    <div class="monogram-seal">
      <p class="monogram-initials">N&amp;L</p>
    </div>
    <p class="couple-names">Nuriya and Laurent</p>
  </main>
</body>
</html>
```